Brixel capital

We lend hard money loans for fixer upper homes and new constructions.Easy Financing on Fix Homes

Target Market(s)

People that need loans & money to buy a Home

Industry/Entity Type

Mortgage Lender

Font styles to use
Serif
Sans Serif

Colors
ffffff
9ccb3b

Requirements
Must have
• Catchy, modern, Clean
Nice to have
• Easy to read

```html
<!DOCTYPE html>
<html lang="en">
<head>
<meta charset="utf-8">
<title>Brixel capital – Stationery</title>
<link href="https://fonts.googleapis.com/css2?family=Mulish:wght@400;600;800&display=swap" rel="stylesheet">
<style>
:root{
  --green:#9ccb3b;
  --green-dark:#3f8a2a;
  --ink:#2b2b2b;
  --text:#555;
  --white:#ffffff;
  --stage:#c4c4c4;
  --card-dark:#232323;
}
*{margin:0;padding:0;box-sizing:border-box}
html,body{width:1200px;height:762px;overflow:hidden}
body{background:var(--stage);font-family:"Mulish",sans-serif;color:var(--text);position:relative}
.abs{position:absolute}
.label{position:absolute;font-size:14px;color:#333;letter-spacing:.5px;transform:translateX(-50%)}
.brand{font-family:"Mulish",sans-serif;font-weight:800;color:var(--ink);line-height:.95;text-align:center;display:flex;flex-direction:column;align-items:center}
.brand .dot{width:var(--d,40px);height:var(--d,40px);border-radius:50%;background:var(--green);margin-bottom:6px}

/* letterhead */
.letter-back{left:94px;top:84px;width:468px;height:634px;background:var(--green)}
.letter{left:23px;top:23px;width:468px;height:661px;background:var(--white)}
.letter .band{position:absolute;left:0;width:100%;height:14px;background:var(--green)}
.letter .band.top{top:0}.letter .band.bottom{bottom:0}
.contact{list-style:none;font-size:7.4px;color:#555}
.contact li{display:flex;align-items:center;gap:4px;height:16px}
.ico{width:8px;height:8px;border-radius:50%;background:var(--green);display:inline-flex;align-items:center;justify-content:center}
.ico svg{width:5px;height:5px}
.letter .contact{position:absolute;left:271px;top:60px}
.letter-date{position:absolute;right:29px;top:220px;font-size:7.4px}
.recipient{position:absolute;left:29px;top:231px;font-size:7.4px;line-height:16.5px}
.body-copy{position:absolute;left:29px;top:287px;width:410px;font-size:7.4px;line-height:12.3px;text-align:justify}
.body-copy p{text-indent:21px;margin-bottom:16px}
.regards{position:absolute;left:29px;top:499px;font-size:7.4px}
.signoff{position:absolute;left:29px;top:573px;font-size:7.4px;line-height:10px}

/* envelope */
.env-open{left:581px;top:140px;width:332px;height:234px;background:#f4f4f4}
.env-open .flap{position:absolute;left:0;top:0;width:100%;height:112px;background:linear-gradient(#6aa84a,var(--green-dark))}
.env-open .pocket{position:absolute;left:0;top:78px;width:100%;height:156px;background:linear-gradient(#fafafa,#e6e6e6)}
.env-closed{left:581px;top:392px;width:332px;height:157px;background:#f7f7f7}
.env-closed .contact{position:absolute;left:220px;top:100px;font-size:4.5px}
.env-closed .contact li{height:10.5px;gap:3px}
.env-closed .ico{width:5px;height:5px}
.seal{left:936px;top:222px;width:246px;height:246px;border-radius:50%;background:#d6d6d6;display:flex;align-items:center;justify-content:center}
.seal-inner{width:224px;height:224px;border-radius:50%;background:var(--white);display:flex;align-items:center;justify-content:center}

/* business cards */
.card{width:220px;height:132px;overflow:hidden}
.card-front{left:582px;top:584px;background:#f5f5f5}
.card-front .dark{position:absolute;left:100px;top:0;width:120px;height:100%;background:var(--card-dark)}
.card-front .name{position:absolute;left:121px;top:34px;color:var(--green);font-weight:800;font-size:9.5px}
.card-front .role{position:absolute;left:129px;top:46px;color:#ddd;font-size:4.5px}
.card-front .rule{position:absolute;left:121px;top:54px;width:58px;height:1px;background:var(--green)}
.card-front .strip{position:absolute;left:95px;top:80px;width:9px;height:46px;background:var(--green)}
.card-front .contact{position:absolute;left:112px;top:80px;color:#ddd;font-size:3.8px}
.card-front .contact li{height:10px}
.card-back{left:822px;top:584px;background:#f5f5f5}
.card-back .dark{position:absolute;left:0;bottom:0;width:100%;height:26px;background:var(--card-dark)}
.card-back .web{position:absolute;left:60px;top:101px;width:100px;height:9px;background:var(--green);color:var(--white);font-size:4.4px;letter-spacing:.4px;text-align:center;line-height:9px}
</style>
</head>
<body>

<!-- Letterhead -->
<div class="abs letter-back"></div>
<section class="abs letter">
  <div class="band top"></div>
  <div class="brand abs" style="left:34px;top:50px;font-size:17px;--d:48px">
    <span class="dot"></span>Brixel<br>capital
  </div>
  <ul class="contact">
    <li><span class="ico"><svg viewBox="0 0 10 10"><circle cx="5" cy="4" r="3" fill="#fff"/></svg></span>48 Harbor Row, Northfield, NY 10011</li>
    <li><span class="ico"><svg viewBox="0 0 10 10"><circle cx="5" cy="4" r="3" fill="#fff"/></svg></span>72 Elmwood Plaza, Rivermont, NY 10420</li>
    <li><span class="ico"><svg viewBox="0 0 10 10"><rect x="3" y="1" width="4" height="8" rx="1" fill="#fff"/></svg></span>(555)010-4821</li>
    <li><span class="ico"><svg viewBox="0 0 10 10"><circle cx="5" cy="5" r="3.5" fill="none" stroke="#fff" stroke-width="1.2"/></svg></span>www.brixelcapitalnow.com</li>
  </ul>
  <div class="letter-date">Date: 21 Aug , 2018</div>
  <div class="recipient">Your Name Here<br>Address</div>
  <div class="body-copy">
    <p>Lorem ipsum dolor sit amet, consectetur adipiscing elit. Suspendisse condimentum egestas tellus et viverra. Vestibulum euismod lacus eget nisi ornare, id laoreet tortor dapibus. Donec lacinia euismod diam, convallis tempus risus. Ut et felis tempor eros blandit feugiat ut non enim. In vestibulum ligula blandit magna blandit dictum. Sed malesuada erat id mauris pretium, eget congue felis interdum. Aenean ultricies enim nec lorem vestibulum, nec commodo quam sagittis. Cras bibendum mauris, eget aliquet semper, libero ipsum ultricies nunc, euismod pellentesque orci risus amet nibh. Maecenas feugiat mi a metus convallis pharetra.</p>
    <p>Duis porta turpis ut pulvinar hendrerit elit lorem vehicula turpis, lacinia semper purus nec nisi. Sed consectetur ante scelerisque tortor pellentesque imperdiet. Pellentesque habitant morbi tristique senectus et netus et malesuada fames ac turpis egestas. Quisque justo turpis, varius ante nec, tincidunt pharetra tellus. Donec non euismod est. Nulla in elit quis tellus mattis feugiat vitae vitae ut magna. Etiam at nisi quis dolor facilisis hendrerit placerat et risus. Vestibulum ut sapien ut justo varius venenatis.</p>
  </div>
  <div class="regards">Regards</div>
  <div class="signoff">Your Name Here<br>Designation Here</div>
  <div class="band bottom"></div>
</section>
<div class="label" style="left:300px;top:726px">LETTERHEAD</div>

<!-- Envelope open -->
<div class="label" style="left:741px;top:110px">ENVELOPE</div>
<div class="abs env-open">
  <div class="flap"></div>
  <div class="pocket"></div>
  <div class="brand abs" style="left:0;width:100%;top:160px;font-size:17px">Brixel capital</div>
</div>
<div class="label" style="left:947px;top:215px">OPEN</div>
<div class="abs seal">
  <div class="seal-inner">
    <div class="brand" style="font-size:25px;--d:64px"><span class="dot"></span>Brixel<br>capital</div>
  </div>
</div>

<!-- Envelope closed -->
<div class="abs env-closed">
  <div class="brand abs" style="left:12px;top:30px;font-size:19px;--d:54px"><span class="dot"></span>Brixel<br>capital</div>
  <ul class="contact">
    <li><span class="ico"></span>48 Harbor Row, Northfield, NY 10011</li>
    <li><span class="ico"></span>72 Elmwood Plaza, Rivermont, NY 10420</li>
    <li><span class="ico"></span>(555)010-4821</li>
    <li><span class="ico"></span>www.brixelcapitalnow.com</li>
  </ul>
</div>
<div class="label" style="left:947px;top:465px">CLOSE</div>

<!-- Business cards -->
<div class="abs card card-front">
  <div class="brand abs" style="left:12px;top:36px;width:76px;font-size:10.5px;--d:32px"><span class="dot"></span>Brixel<br>capital</div>
  <div class="dark"></div>
  <div class="name">YOUR NAME</div>
  <div class="role">Designation Here</div>
  <div class="rule"></div>
  <div class="strip"></div>
  <ul class="contact">
    <li>48 Harbor Row, Northfield, NY 10011</li>
    <li>72 Elmwood Plaza, Rivermont, NY 10420</li>
    <li>(555)010-4821</li>
    <li>www.brixelcapitalnow.com</li>
  </ul>
</div>
<div class="label" style="left:691px;top:726px">FRONT</div>

<div class="abs card card-back">
  <div class="brand abs" style="left:0;width:100%;top:28px;font-size:10.5px;--d:32px"><span class="dot"></span>Brixel<br>capital</div>
  <div class="dark"></div>
  <div class="web">www.brixelcapitalnow.com</div>
</div>
<div class="label" style="left:931px;top:726px">BACK</div>

</body>
</html>
```